Personalised Poetry business needs a business card designed

I am a writer that specialises in personalised poetry for people for significant life events.
I want a business card that stands out and portrays class and professionalism but is also welcoming & indicates warmth and honesty.
I'm happy with the logo that was designed for me, I would like to see it in raised print on the business card. I am open to suggestions on colours but think perhaps gold or silver writing for the logo would look good. I would like just the logo and my name and contact details on the front of the card. On the back of the card, I would like a list of the different events I provide poems for I will upload a photo of my current business card for reference. My current logo has a shading behind it that I don't like, I just want the words of the logo without any background colour

Target Market(s)

People wanting to provide a unique gift to someone special in their life

Industry/Entity Type

Writer

Contact Information for Business Card

Logo, my name and contact details on the front and a list of all the events I write poetry for on the back

Font styles to use
Script

Requirements
Must have
• I would like to see the logo, if possible, in a raised type of print on the card so that you can feel the actual words. I would like to have a glossy finish to the card and be able to print it on good quality board
Should not have
• The shading that is currently behind the logo on my current business card

```html
<!DOCTYPE html>
<html lang="en">
<head>
<meta charset="utf-8">
<title>Lines for Always – Business Card</title>
<link rel="stylesheet" href="https://fonts.googleapis.com/css2?family=Montserrat:wght@400;500;700&family=Arimo:wght@400;700&display=swap">
<style>
  :root {
    --backdrop: #3a3a3a;
    --card-white: #ffffff;
    --card-dark: #2b2b2b;
    --ink: #1f1f1f;
    --ink-soft: #3c3c3c;
    --band-dark: #2e2e2e;
    --band-grey: #a39e9f;
    --gold: #c9a22a;
    --gold-light: #e0bd45;
    --text-light: #f4f4f4;
  }
  * { box-sizing: border-box; margin: 0; padding: 0; }
  html, body { width: 1200px; height: 803px; overflow: hidden; }
  body {
    background: var(--backdrop);
    font-family: "Montserrat", sans-serif;
    position: relative;
  }
  .card {
    position: absolute;
    top: 250px;
    width: 520px;
    height: 300px;
    border-radius: 18px;
    overflow: hidden;
  }

  /* Front */
  .card-front { left: 50px; background: var(--card-white); }
  .front-brand {
    position: absolute; left: 36px; top: 104px; width: 220px; text-align: center;
  }
  .front-brand .brand-name {
    font-family: "Montserrat", sans-serif; font-weight: 500;
    font-size: 24px; color: var(--ink); letter-spacing: 0.5px;
  }
  .front-brand .brand-tagline {
    font-size: 11px; color: var(--ink-soft); margin-top: 6px; letter-spacing: 0.5px;
  }
  .front-divider { position: absolute; left: 262px; top: 70px; }
  .contact { position: absolute; left: 300px; top: 62px; }
  .contact-name {
    font-family: "Arimo", sans-serif; font-weight: 700; font-size: 22px; color: var(--ink);
  }
  .contact-line {
    display: flex; align-items: center; gap: 8px;
    font-family: "Arimo", sans-serif; font-size: 12px; color: var(--ink-soft);
    margin-top: 8px;
  }
  .contact-line:first-of-type { margin-top: 14px; }
  .contact-line svg { width: 12px; height: 12px; fill: var(--ink); }
  .front-band {
    position: absolute; left: 0; top: 238px; width: 420px; height: 34px;
    background: var(--band-dark);
    color: var(--text-light); font-size: 13px; letter-spacing: 3px;
    display: flex; align-items: center; padding-left: 40px;
  }
  .front-accent {
    position: absolute; right: 0; top: 238px; width: 72px; height: 34px;
    background: var(--band-grey);
  }

  /* Back */
  .card-back { left: 630px; background: var(--card-dark); }
  .back-brand { position: absolute; left: 0; right: 0; top: 56px; text-align: center; }
  .back-brand .brand-mark {
    display: inline-block; width: 14px; height: 14px; border-radius: 50%;
    background: var(--gold); vertical-align: middle; margin-right: 10px;
  }
  .back-brand .brand-name {
    font-weight: 500; font-size: 38px; color: var(--gold); vertical-align: middle;
  }
  .back-brand .brand-tagline {
    font-size: 16px; color: var(--gold); margin-top: 8px; letter-spacing: 0.5px;
  }
  .events { position: absolute; left: 34px; right: 34px; top: 186px; }
  .events-heading {
    font-weight: 700; font-size: 14px; color: var(--gold); letter-spacing: 0.3px;
    padding-bottom: 6px; border-bottom: 1px solid var(--gold);
  }
  .events-list {
    list-style: none; margin-top: 10px; color: var(--text-light);
    font-size: 12.5px; font-weight: 500; line-height: 1.6;
  }
  .events-list .dot { color: var(--gold-light); margin: 0 5px; }
</style>
</head>
<body>
  <section class="card card-front" aria-label="Card front">
    <div class="front-brand">
      <div class="brand-name">Lines for Always</div>
      <div class="brand-tagline">Personalised Poetry</div>
    </div>
    <svg class="front-divider" width="30" height="60" viewBox="0 0 30 60" aria-hidden="true">
      <line x1="2" y1="2" x2="28" y2="58" stroke="#9a9a9a" stroke-width="1"/>
    </svg>
    <div class="contact">
      <div class="contact-name">Owen Hartley</div>
      <div class="contact-line">
        <svg viewBox="0 0 24 24" aria-hidden="true"><path d="M6.6 10.8a15 15 0 0 0 6.6 6.6l2.2-2.2a1 1 0 0 1 1-.25 11.4 11.4 0 0 0 3.6.57 1 1 0 0 1 1 1V20a1 1 0 0 1-1 1A17 17 0 0 1 3 4a1 1 0 0 1 1-1h3.5a1 1 0 0 1 1 1c0 1.25.2 2.45.57 3.57a1 1 0 0 1-.25 1z"/></svg>
        <span>0400 555 123</span>
      </div>
      <div class="contact-line">
        <svg viewBox="0 0 24 24" aria-hidden="true"><path d="M2 5h20v14H2z M2 5l10 8 10-8" fill="none" stroke="#1f1f1f" stroke-width="2"/></svg>
        <span>owen@linesforalways.com</span>
      </div>
    </div>
    <div class="front-band">www.linesforalways.com</div>
    <div class="front-accent"></div>
  </section>

  <section class="card card-back" aria-label="Card back">
    <div class="back-brand">
      <span class="brand-mark"></span><span class="brand-name">Lines for Always</span>
      <div class="brand-tagline">Personalised Poetry</div>
    </div>
    <div class="events">
      <div class="events-heading">MOMENTOUS LIFE EVENTS PERSONALISED IN POETRY</div>
      <ul class="events-list">
        <li>Weddings &amp; Anniversaries<span class="dot">•</span>Birthdays &amp; Christmas<span class="dot">•</span>Valentines Day</li>
        <li>Retirements, Business &amp; Corporate Events<span class="dot">•</span>Funerals &amp; Eulogies</li>
      </ul>
    </div>
  </section>
</body>
</html>
```